Tall Fern Software PowerPoint template

We are a software company selling endpoint visibility, access and security technology to enterprise-level IT departments.
Our technology helps organizations gain comprehensive visibility into and control over devices accessing their corporate network so they can quickly identify and address suspicious activity on the network that could lead to potential threats like data breaches.
This technology can cost organizations upwards of $1M - depending on the size of the organization. Our primary clients are Marquee 3,000 companies.
We want a professional, polished PowerPoint template that we can use for all company presentations. Please include:
Title page
Section page
General info page
Thank you page
Logo options and color specs are attached.
Please include our tagline on at least the title page: Chart the frontier. Steady the core.
Software

```html
<!DOCTYPE html>
<html lang="en">
<head>
<meta charset="utf-8">
<title>Tall Fern Software – Thank You Slide</title>
<link rel="stylesheet" href="https://fonts.googleapis.com/css2?family=Open+Sans:wght@400;600;700&family=Ubuntu:wght@500&display=swap">
<style>
  :root {
    --rust: #b35c3f;
    --rust-deep: #a0432f;
    --crimson: #8f1d24;
    --ink: #1a1a1a;
    --mist: #e8e9eb;
    --rule: #c8c8c8;
    --paper: #ffffff;
    --muted: #555555;
  }
  * { margin: 0; padding: 0; box-sizing: border-box; }
  html, body { width: 1200px; height: 849px; overflow: hidden; background: var(--paper); }
  body { font-family: "Open Sans", Arial, sans-serif; color: var(--ink); }

  .slide { position: relative; width: 1200px; height: 849px; background: var(--paper); overflow: hidden; }

  .heading-bar { position: absolute; left: 134px; top: 0; width: 7px; height: 87px; background: var(--crimson); }
  .slide-heading { position: absolute; left: 163px; top: 36px; }
  .slide-title { font-size: 20px; font-weight: 400; color: var(--crimson); letter-spacing: 0.2px; line-height: 26px; }
  .slide-date { font-size: 19px; font-weight: 600; color: var(--ink); line-height: 26px; }

  .corner-accent {
    position: absolute; right: 0; top: 0; width: 372px; height: 364px;
    background: radial-gradient(ellipse at 72% 20%, rgba(179,92,63,0.55) 0%, rgba(179,92,63,0.25) 40%, rgba(232,233,235,0.6) 65%, rgba(255,255,255,0) 85%);
  }

  .thanks-disc {
    position: absolute; left: 105px; top: 192px; width: 500px; height: 500px;
    border-radius: 50%; background: var(--rust);
    display: flex; align-items: center; justify-content: center;
  }
  .thanks-text { font-family: "Ubuntu", "Open Sans", sans-serif; font-weight: 500; font-size: 64px; color: var(--paper); letter-spacing: 0.5px; margin-right: 12px; }

  .contact { position: absolute; left: 652px; top: 387px; }
  .contact-name { font-size: 19px; font-weight: 700; color: var(--rust); margin-bottom: 14px; }
  .contact-line { font-size: 15.5px; line-height: 24px; color: var(--ink); }

  .footer-rule { position: absolute; left: 128px; top: 771px; width: 713px; height: 1px; background: var(--rule); }
  .copyright { position: absolute; left: 134px; top: 779px; font-size: 11px; color: var(--muted); }

  .brand { position: absolute; left: 858px; top: 748px; display: flex; align-items: center; gap: 16px; }
  .brand-dot { width: 40px; height: 40px; border-radius: 50%; background: var(--rust); }
  .brand-name { font-size: 25px; font-weight: 600; color: var(--crimson); letter-spacing: 4px; line-height: 28px; }
</style>
</head>
<body>
<main class="slide">
  <div class="heading-bar"></div>
  <header class="slide-heading">
    <p class="slide-title">PPT HEADING GOES HERE</p>
    <p class="slide-date">FEB, 2015</p>
  </header>

  <div class="corner-accent" role="img" aria-label="Decorative pattern of rust and light grey circles"></div>

  <div class="thanks-disc">
    <h1 class="thanks-text">Thank you</h1>
  </div>

  <address class="contact" style="font-style: normal;">
    <p class="contact-name">Tall Fern INC</p>
    <p class="contact-line">402 Cedar Row #12 (rear entry)</p>
    <p class="contact-line">Aldenford, NM 87521</p>
    <p class="contact-line">505 555-0147</p>
    <p class="contact-line">www.tallfernsw.com</p>
  </address>

  <div class="footer-rule"></div>
  <p class="copyright">©2015 Tall Fern Software</p>

  <div class="brand">
    <span class="brand-dot"></span>
    <span class="brand-name">TALL FERN<br>SOFTWARE</span>
  </div>
</main>
</body>
</html>
```